Bramblewick Systems Group - IT Services Company/Managed Services/Consulting Card Design

Our company needs a business card design that will appeal to client companies with 50-1000 employees. We do IT services, administration, management, projects, budgeting and consulting (Like a small Corvatel.com, Plumvary.com or Tundrabox.com). Mainly helping businesses use technology to be more competitive and efficient. We work with IT Infrastructure, switches, routers, firewalls and Cloud, Verlanta/Linux servers, Quellon server virtualization, Datacenter environments, Email systems, Business Systems, Backup, Disaster Recovery, Data Security, NVX, Deskora 12 and Halcyte.) Would like the final design to be professional but stand out to our prospective clients. Our current logo is attached. Color or design could be changed. Overall looking for a great finished product, original ideas are welcome and would pay more for the right one. If you think you have a better logo idea include a general idea if you can. Web design has not been done yet so that is a later possibility too.

Target Market(s)

1st - Mid-sized companies with 100-1000 employees with technology needs
2nd - Smaller companies with 20-99 employees with technology needs
- These companies can be in many different industries. Heathcare, legal, manufacturing, education, non-profit, services

Industry/Entity Type

Information Technology

Contact Information for Business Card

Should include the following info:

Logo or other logo with Company Name

Martin J. Cosgrove

Principal

BramblewickSys.com

mcosgrove@BramblewickSys.com

(866) 7-BRAMBLE x 348

Font styles to use
Other font styles liked:
• designer can decide

Requirements
Must have
• Professional, appealing design, appeal to the target market
Nice to have
• Some sort of additional accent design that would stand out could be nice. I thought of adding a graphic in the top left corner that would look like the corner of the card was becoming more and more pixelated as it got near the corner, with some pixels missing.

```html
<!DOCTYPE html>
<html lang="en">
<head>
<meta charset="utf-8">
<title>Bramblewick Systems Group – Business Card</title>
<link rel="stylesheet" href="https://fonts.googleapis.com/css2?family=PT+Serif:wght@400;700&family=Open+Sans:wght@400;600&display=swap">
<style>
  :root {
    --brand-blue: #1f74bb;
    --ink-dark: #231f20;
    --paper: #ffffff;
    --stage: #e9e9e7;
    --name-blue: #2a6fb0;
  }
  * { box-sizing: border-box; margin: 0; padding: 0; }
  html, body { width: 1200px; height: 1120px; overflow: hidden; }
  body { background: var(--stage); position: relative; font-family: "Open Sans", sans-serif; }

  .card {
    position: absolute;
    width: 560px;
    height: 320px;
    overflow: hidden;
    box-shadow: 0 6px 18px rgba(0,0,0,0.18);
  }

  /* Front */
  .card-front { left: 110px; top: 110px; background: var(--paper); }
  .front-bands { position: absolute; inset: 0; }
  .wordmark {
    position: absolute;
    left: 34px;
    top: 28px;
    font-family: "PT Serif", serif;
    font-weight: 700;
    color: var(--ink-dark);
    line-height: 1;
  }
  .wordmark-main { display: block; font-size: 40px; letter-spacing: 0.5px; }
  .wordmark-sub { display: block; font-size: 17px; letter-spacing: 3.4px; margin-top: 4px; }
  .tagline {
    position: absolute;
    left: 34px;
    top: 102px;
    font-size: 12.5px;
    letter-spacing: 1.6px;
    color: var(--brand-blue);
  }
  .person { position: absolute; left: 34px; top: 138px; font-family: "PT Serif", serif; line-height: 1.25; }
  .person-name { font-size: 19px; font-weight: 700; color: var(--name-blue); letter-spacing: 0.6px; }
  .person-title { font-size: 16px; color: var(--ink-dark); margin-top: 2px; }

  .contact-list { position: absolute; left: 36px; top: 230px; list-style: none; color: var(--paper); font-size: 13.5px; }
  .contact-list li { display: flex; align-items: center; gap: 10px; height: 24px; }
  .contact-list svg { width: 13px; height: 13px; flex: none; }

  /* Back */
  .card-back { left: 530px; top: 680px; background: var(--brand-blue); color: var(--paper); text-align: center; }
  .card-back .wordmark {
    position: static;
    color: var(--paper);
    margin-top: 72px;
  }
  .card-back .wordmark-main { font-size: 46px; }
  .card-back .wordmark-sub { font-size: 19px; letter-spacing: 4px; margin-top: 6px; }
  .card-back .tagline { position: static; color: var(--paper); font-size: 14px; letter-spacing: 2px; margin-top: 12px; }
  .back-url { font-size: 17px; letter-spacing: 4px; margin-top: 34px; }
</style>
</head>
<body>

<section class="card card-front" aria-label="Business card front">
  <svg class="front-bands" viewBox="0 0 560 320" width="560" height="320" aria-hidden="true">
    <path d="M0,198 H338 Q354,198 362,210 L436,320 H0 Z" fill="var(--ink-dark)"/>
    <path d="M0,207 H330 Q346,207 354,219 L422,320 H0 Z" fill="var(--brand-blue)"/>
    <path d="M456,192 H560 V320 H514 L444,216 V204 Q444,192 456,192 Z" fill="var(--ink-dark)"/>
  </svg>

  <div class="wordmark">
    <span class="wordmark-main">BRAMBLEWICK</span>
    <span class="wordmark-sub">SYSTEMS GROUP</span>
  </div>
  <p class="tagline">PLANNED. CONNECTED. REFINED.</p>

  <div class="person">
    <p class="person-name">MARTIN J. COSGROVE</p>
    <p class="person-title">PRINCIPAL</p>
  </div>

  <ul class="contact-list">
    <li>
      <svg viewBox="0 0 16 16" aria-hidden="true"><circle cx="8" cy="8" r="7.2" fill="none" stroke="#fff" stroke-width="1.4"/><path d="M5.5,4.5 L7,4.5 L7.6,6.6 L6.7,7.3 Q7.5,9 8.8,9.6 L9.5,8.7 L11.5,9.3 L11.5,10.8 Q8,11.5 5.5,4.5 Z" fill="#fff"/></svg>
      (866) 7-BRAMBLE x 348
    </li>
    <li>
      <svg viewBox="0 0 16 16" aria-hidden="true"><circle cx="8" cy="8" r="7.6" fill="#fff"/><rect x="4" y="5.5" width="8" height="5.5" fill="var(--brand-blue)"/><path d="M4,5.5 L8,8.6 L12,5.5" fill="none" stroke="#fff" stroke-width="0.9"/></svg>
      mcosgrove@BramblewickSys.com
    </li>
    <li>
      <svg viewBox="0 0 16 16" aria-hidden="true"><g fill="none" stroke="#fff" stroke-width="1.2"><circle cx="8" cy="8" r="6.6"/><ellipse cx="8" cy="8" rx="2.8" ry="6.6"/><path d="M1.4,8 H14.6 M2.6,4.6 H13.4 M2.6,11.4 H13.4"/></g></svg>
      www.bramblewicksys.com
    </li>
  </ul>
</section>

<section class="card card-back" aria-label="Business card back">
  <div class="wordmark">
    <span class="wordmark-main">BRAMBLEWICK</span>
    <span class="wordmark-sub">SYSTEMS GROUP</span>
  </div>
  <p class="tagline">PLANNED. CONNECTED. REFINED.</p>
  <p class="back-url">www.bramblewicksys.com</p>
</section>

</body>
</html>
```